Letterhead for clinic notes, test reports, and business cards

I need business card and letterheads for a medical clinic with the following:
1- Business cards. The back should allow for space for date and time of next appointments (few lines would do)
2- Letterhead for clinic notes
3- Letterhead for test reports.

Feel free to use whats included for examples. I value creativity so be creative.

Target Market(s)

Patients, referring physicians.

Industry/Entity Type

Health Care

Requirements
Must have
• Must use current logo.
• Must look good on white background
• Letterhead and reports must look good faxed.
• Please use themes of the current logo. Another possible color to use is grey as well (www.brambleveincare.org - use the font color in the text of that website)

```html
<!DOCTYPE html>
<html lang="en">
<head>
<meta charset="utf-8">
<title>Bramblevein Heart Centre – Stationery</title>
<link href="https://fonts.googleapis.com/css2?family=Cinzel:wght@500&family=Questrial&family=Oswald:wght@500&display=swap" rel="stylesheet">
<style>
  :root{
    --bg:#d3d3d3;
    --paper:#f1f1f1;
    --navy:#1b3a7a;
    --blue-deep:#0a3d86;
    --blue:#0575bd;
    --cyan:#06a2da;
    --red:#b3161b;
    --grey-text:#4a4a4a;
    --rule:#9a9a9a;
  }
  *{box-sizing:border-box;margin:0;padding:0}
  html,body{width:1200px;height:1041px;overflow:hidden;background:var(--bg)}
  body{position:relative;font-family:"Questrial",sans-serif;color:var(--grey-text)}
  .sheet{position:absolute;background:var(--paper);box-shadow:0 1px 3px rgba(0,0,0,.25)}
  .brand{font-family:"Cinzel",serif;font-weight:500;color:var(--navy);text-align:center;line-height:1}
  .wave{position:absolute;left:0;bottom:0;width:100%;display:block}

  /* Folder */
  .folder{left:166px;top:76px;width:417px;height:541px;border-radius:3px;
    background:linear-gradient(200deg,var(--cyan) 0%,var(--blue) 30%,var(--blue-deep) 70%,#2a2470 100%)}
  .folder-spine{position:absolute;left:26px;top:0;bottom:0;width:6px;background:rgba(0,0,0,.08);border-left:1px solid rgba(255,255,255,.1)}
  .folder .brand{position:absolute;left:0;right:0;top:128px;color:#fff}
  .folder .brand-main{font-size:23px;letter-spacing:.5px}
  .folder .brand-sub{font-size:17px;margin-top:3px}
  .folder-dot{position:absolute;left:50%;top:70px;width:36px;height:36px;margin-left:-18px;border-radius:50%;background:rgba(255,255,255,.9)}
  .folder-url{position:absolute;left:0;right:0;bottom:22px;text-align:center;color:#fff;font-size:8px}

  /* Letterhead */
  .letter{left:615px;top:95px;width:403px;height:522px}
  .letter .brand{position:absolute;left:32px;top:60px;width:100px}
  .brand-mark{width:18px;height:18px;border-radius:50%;background:var(--red);margin:0 auto 6px}
  .letter .brand-main{font-size:10.5px}
  .letter .brand-sub{font-size:8px;margin-top:1px}
  .contact{position:absolute;list-style:none;font-size:5.2px;line-height:7px;color:var(--grey-text)}
  .contact li{display:flex;align-items:center;gap:3px}
  .contact svg{width:5px;height:5px;flex:none}
  .letter .contact{left:291px;top:32px}
  .address{font-size:5.2px;line-height:7px}
  .letter .address-top{position:absolute;left:291px;top:63px}
  .letter-body{position:absolute;left:32px;top:114px;width:340px;font-size:5.4px;line-height:7px}
  .letter-body p{margin-bottom:7px}
  .salutation{font-weight:bold;color:#222}
  .sign{display:flex;align-items:flex-start;gap:8px;margin-top:4px}
  .signature{width:80px;height:30px;background:linear-gradient(90deg,rgba(40,70,170,.12),rgba(40,70,170,.04))}

  /* Envelopes */
  .env-front{left:132px;top:645px;width:451px;height:196px}
  .env-front .brand{position:absolute;left:26px;top:18px;width:100px}
  .env-front .brand-main{font-size:10.5px}
  .env-front .brand-sub{font-size:8px;margin-top:1px}
  .env-front .address{position:absolute;left:18px;top:71px;width:116px;text-align:center}
  .env-back{left:615px;top:645px;width:451px;height:196px}
  .flap{position:absolute;left:0;top:0;width:100%;height:64px;display:block}
  .env-back .brand-mark{position:absolute;left:50%;top:18px;margin:0 0 0 -11px;width:22px;height:22px;background:#fff}

  /* Cards */
  .appt{left:416px;top:869px;width:166px;height:96px}
  .appt .brand{position:absolute;left:15px;top:12px;width:62px}
  .appt .brand-main{font-size:6.8px}
  .appt .brand-sub{font-size:5px}
  .appt-title{position:absolute;right:15px;top:13px;font-family:"Oswald",sans-serif;font-weight:500;font-size:6.3px;color:var(--red)}
  .field{position:absolute;font-size:4.3px;color:#333;display:flex;align-items:flex-end;gap:2px}
  .field span.line{border-bottom:.6px solid var(--rule);height:4px}
  .days{position:absolute;left:15px;top:73px;display:flex;gap:8px;font-size:3.8px;font-weight:bold;color:#333}
  .days span{display:flex;align-items:center;gap:2px}
  .days i{display:inline-block;width:5px;height:5px;border:.6px solid #333}
  .appt-note{position:absolute;left:15px;top:86px;font-size:4px;color:#333}

  .bcard{left:615px;top:869px;width:167px;height:96px}
  .bcard .brand{position:absolute;left:10px;top:26px;width:72px}
  .bcard .brand-mark{width:14px;height:14px;margin-bottom:4px}
  .bcard .brand-main{font-size:7.4px}
  .bcard .brand-sub{font-size:5.4px}
  .person{position:absolute;left:97px;top:20px}
  .person-name{font-size:5.2px;font-weight:bold;color:var(--navy);letter-spacing:.2px}
  .person-role{font-size:3.8px;margin-bottom:5px}
  .bcard .contact{font-size:3.8px;line-height:5.3px}
  .bcard .contact svg{width:4px;height:4px}
  .bcard .address{font-size:3.8px;line-height:5.3px;margin-top:3px}
</style>
</head>
<body>

<svg width="0" height="0" style="position:absolute" aria-hidden="true">
  <defs>
    <linearGradient id="waveBlue" x1="0" x2="1">
      <stop offset="0" stop-color="#16357e"/><stop offset=".6" stop-color="#0a5fb0"/><stop offset="1" stop-color="#06a2da"/>
    </linearGradient>
    <linearGradient id="waveRed" x1="0" x2="1">
      <stop offset="0" stop-color="#a3121a"/><stop offset=".7" stop-color="#c9241f"/><stop offset="1" stop-color="#ef7a5f"/>
    </linearGradient>
    <symbol id="wave" viewBox="0 0 400 40" preserveAspectRatio="none">
      <path d="M0 40V20C130 6 280 -2 400 20V32C280 10 150 14 40 40Z" fill="url(#waveRed)"/>
      <path d="M120 40C200 20 300 10 400 30V40Z" fill="url(#waveBlue)"/>
      <path d="M40 40C150 14 280 10 400 32" fill="none" stroke="#fff" stroke-width="1.2"/>
    </symbol>
    <symbol id="ico-phone" viewBox="0 0 10 10"><rect width="10" height="10" rx="1" fill="#b3161b"/><path d="M3 2l1.2 1.4-.7.9c.5 1 1.2 1.7 2.2 2.2l.9-.7L8 7 7 8C4.5 7.6 2.4 5.5 2 3z" fill="#fff"/></symbol>
    <symbol id="ico-mail" viewBox="0 0 10 10"><rect width="10" height="10" rx="1" fill="#b3161b"/><path d="M2 3h6v4H2zM2 3l3 2.2L8 3" fill="none" stroke="#fff" stroke-width=".8"/></symbol>
    <symbol id="ico-web" viewBox="0 0 10 10"><rect width="10" height="10" rx="1" fill="#b3161b"/><circle cx="5" cy="5" r="2.8" fill="none" stroke="#fff" stroke-width=".8"/><path d="M2.2 5h5.6M5 2.2v5.6" stroke="#fff" stroke-width=".6"/></symbol>
  </defs>
</svg>

<!-- Presentation folder -->
<section class="sheet folder">
  <div class="folder-spine"></div>
  <div class="folder-dot"></div>
  <div class="brand">
    <div class="brand-main">BRAMBLEVEIN HEART</div>
    <div class="brand-sub">CENTRE</div>
  </div>
  <div class="folder-url">www.brambleveincare.org</div>
</section>

<!-- Letterhead -->
<section class="sheet letter">
  <div class="brand">
    <div class="brand-mark"></div>
    <div class="brand-main">BRAMBLEVEIN HEART</div>
    <div class="brand-sub">CENTRE</div>
  </div>
  <ul class="contact">
    <li><svg><use href="#ico-phone"/></svg>555-014-2200</li>
    <li><svg><use href="#ico-phone"/></svg>555-014-2201</li>
    <li><svg><use href="#ico-mail"/></svg>contact@brambleveincare.org</li>
    <li><svg><use href="#ico-web"/></svg>www.brambleveincare.org</li>
  </ul>
  <div class="address address-top">1180 Larkfield Road, Suite 40<br>Ashbury ON K0L2B4</div>
  <div class="letter-body">
    <p>30.09.2016</p>
    <p>Recipient's name<br>Lindenhof 7<br>20144 Hamburg<br>Germany</p>
    <p style="margin-top:28px" class="salutation">Dear sir,</p>
    <p>Thank you for referring your patient to our cardiology team. This letter confirms the findings from the recent consultation and outlines the plan we discussed together during the visit.</p>
    <p>The resting electrocardiogram showed a regular rhythm with no acute changes. Blood pressure remained within the expected range, and the echocardiogram revealed normal valve function and a healthy ejection fraction. A follow-up stress test has been booked to complete the assessment, and results will be forwarded to your office.</p>
    <p>Please continue current medications unless new symptoms appear. Our nurses remain available for any questions from you or the patient.</p>
    <p>We appreciate your trust and look forward to continued collaboration in caring for your patients and their families.</p>
    <div class="sign">
      <div>Yours Sincerely,<br><b style="color:#222">Ilse Varnow</b></div>
      <div class="signature" role="img" aria-label="Handwritten signature"></div>
    </div>
  </div>
  <svg class="wave" height="36"><use href="#wave"/></svg>
</section>

<!-- Envelope front -->
<section class="sheet env-front">
  <div class="brand">
    <div class="brand-mark"></div>
    <div class="brand-main">BRAMBLEVEIN HEART</div>
    <div class="brand-sub">CENTRE</div>
  </div>
  <div class="address">1180 Larkfield Road, Suite 40<br>Ashbury ON K0L2B4</div>
  <svg class="wave" height="30"><use href="#wave"/></svg>
</section>

<!-- Envelope back -->
<section class="sheet env-back">
  <svg class="flap" viewBox="0 0 451 64" preserveAspectRatio="none">
    <defs><linearGradient id="flapGrad" x1="0" x2="1"><stop offset="0" stop-color="#0a5aa8"/><stop offset="1" stop-color="#06a2da"/></linearGradient></defs>
    <path d="M0 0H451L440 62Q439 64 436 64H15Q12 64 11 62Z" fill="url(#flapGrad)"/>
  </svg>
  <div class="brand-mark"></div>
</section>

<!-- Appointment card -->
<section class="sheet appt">
  <div class="brand">
    <div class="brand-main">BRAMBLEVEIN HEART</div>
    <div class="brand-sub">CENTRE</div>
  </div>
  <div class="appt-title">APPOINTMENT CARD</div>
  <div class="field" style="left:15px;top:38px">NAME <span class="line" style="width:120px"></span></div>
  <div class="field" style="left:15px;top:53px">DATE <span class="line" style="width:50px"></span></div>
  <div class="field" style="left:88px;top:53px">TIME <span class="line" style="width:34px"></span> AM &nbsp;PM</div>
  <div class="days">
    <span><i></i>MON.</span><span><i></i>TUES.</span><span><i></i>WED.</span><span><i></i>THUR.</span><span><i></i>FRI.</span><span><i></i>SAT.</span>
  </div>
  <div class="appt-note">If you are unable to keep your appointment, please call us within 24 hours.</div>
</section>

<!-- Business card -->
<section class="sheet bcard">
  <div class="brand">
    <div class="brand-mark"></div>
    <div class="brand-main">BRAMBLEVEIN HEART</div>
    <div class="brand-sub">CENTRE</div>
  </div>
  <div class="person">
    <div class="person-name">NOAH PELLERING</div>
    <div class="person-role">General Manager</div>
    <ul class="contact" style="position:static">
      <li><svg><use href="#ico-phone"/></svg>555-014-2200</li>
      <li><svg><use href="#ico-phone"/></svg>555-014-2201</li>
      <li><svg><use href="#ico-mail"/></svg>contact@brambleveincare.org</li>
      <li><svg><use href="#ico-web"/></svg>www.brambleveincare.org</li>
    </ul>
    <div class="address">1180 Larkfield Road, Suite 40<br>Ashbury ON K0L2B4</div>
  </div>
  <svg class="wave" height="14"><use href="#wave"/></svg>
</section>

</body>
</html>
```